Theater poster for a play about the Harwick siblings

We need a poster to promote our theatre show, Lanterns at Dusk: The Harwicks. We want an image that is edgy, modern, and hip. The show plays with the contrast between the modern age and the Victorian time period, so a possible design could reflect that. We are looking for an image that is more evocative and abstract, rather than something realistic like a photograph. The play deals with themes of alcoholism, incest, and incorporates the siblings' novels and poetry. We are also using kimonos from Japan so a possible design could also reference art or culture from there, but it must be in a very subtle way. The color red should be incorporated in a very strong way. The font should be very modern and hip.

```html
<!DOCTYPE html>
<html lang="en">
<head>
<meta charset="utf-8">
<title>Lanterns at Dusk: The Harwicks</title>
<link href="https://fonts.googleapis.com/css2?family=Libre+Baskerville&family=Advent+Pro:wght@200;300&display=swap" rel="stylesheet">
<style>
  :root {
    --red: #d3121d;
    --red-bright: #e8222b;
    --red-deep: #8a0710;
    --ink: #130606;
    --white: #ffffff;
    --skin: #ecc7a8;
    --skin-shade: #c98f72;
    --fan-blue: #3f86b8;
    --fan-navy: #2c3f6e;
    --mist: #c4cadf;
    --couple-red: #e2333b;
  }
  * { margin: 0; padding: 0; box-sizing: border-box; }
  html, body { width: 850px; height: 1200px; overflow: hidden; background: var(--red-deep); }
  .poster {
    position: relative;
    width: 850px;
    height: 1200px;
    overflow: hidden;
    background: linear-gradient(180deg, var(--red-bright) 0%, var(--red) 22%, #b4101b 60%, var(--red-deep) 100%);
  }
  .artwork {
    position: absolute;
    left: 0; top: 200px;
    width: 830px; height: 814px;
    background:
      radial-gradient(ellipse 30% 22% at 47% 82%, var(--couple-red) 0%, rgba(226,51,59,0.92) 55%, rgba(226,51,59,0) 100%),
      radial-gradient(ellipse 24% 18% at 36% 76%, #f06a6a 0%, rgba(240,106,106,0) 100%),
      radial-gradient(ellipse 27% 30% at 18% 55%, var(--fan-blue) 0%, var(--fan-navy) 55%, rgba(44,63,110,0) 100%),
      radial-gradient(ellipse 28% 34% at 58% 34%, var(--skin) 0%, #e4b797 50%, rgba(201,143,114,0) 100%),
      radial-gradient(ellipse 22% 14% at 40% 18%, #3a2222 0%, rgba(58,34,34,0) 100%),
      linear-gradient(90deg, rgba(196,202,223,0.9) 0%, rgba(210,214,228,0.85) 70%, rgba(190,196,218,0.8) 100%);
    -webkit-mask-image: linear-gradient(180deg, transparent 0%, #000 14%, #000 100%);
            mask-image: linear-gradient(180deg, transparent 0%, #000 14%, #000 100%);
  }
  .edge-strip {
    position: absolute;
    top: 0; right: 0;
    width: 20px; height: 1014px;
    background: linear-gradient(180deg, #b30e18, #7e0710);
  }
  .title {
    position: absolute;
    left: 0; top: 32px;
    width: 850px;
    text-align: center;
    font-family: "Libre Baskerville", Georgia, serif;
    font-weight: 400;
    line-height: 1;
  }
  .title-lead {
    display: block;
    color: var(--ink);
    font-size: 80px;
    letter-spacing: -1px;
  }
  .title-family {
    display: block;
    margin-top: 30px;
    color: var(--white);
    font-size: 94px;
  }
  .details {
    position: absolute;
    left: 0; bottom: 0;
    width: 850px; height: 186px;
    background: linear-gradient(90deg, var(--red-deep) 0%, #b10c16 45%, var(--red) 100%);
    color: var(--white);
    font-family: "Advent Pro", "Arial Narrow", sans-serif;
  }
  .date {
    position: absolute;
    left: 88px; top: 16px;
    font-size: 88px;
    font-weight: 200;
    letter-spacing: 1px;
    line-height: 1;
    white-space: nowrap;
  }
  .rule {
    position: absolute;
    left: 90px; top: 104px;
    width: 645px; height: 2px;
    background: var(--white);
  }
  .venue, .code {
    position: absolute;
    top: 114px;
    font-size: 40px;
    font-weight: 300;
    line-height: 1;
    white-space: nowrap;
  }
  .venue { left: 90px; letter-spacing: 12px; }
  .code { right: 105px; letter-spacing: 10px; margin-right: -10px; }
</style>
</head>
<body>
  <main class="poster">
    <div class="artwork" role="img" aria-label="Collage: a woman's face with a dangling earring half hidden behind a blue folding fan, and a red-tinted couple in Victorian dress embracing in the foreground"></div>
    <div class="edge-strip"></div>
    <h1 class="title">
      <span class="title-lead">Lanterns at Dusk:</span>
      <span class="title-family">The Harwicks</span>
    </h1>
    <footer class="details">
      <p class="date">SEPTEMBER 8, 2014</p>
      <div class="rule"></div>
      <p class="venue">CITY THEATRE</p>
      <p class="code">2231 CS</p>
    </footer>
  </main>
</body>
</html>
```